Construction company- stationary project
business card, letterhead, envelopes, presentation folder
Construction company- stationary project -
Creative Brief
Professional
Brent Halloway
38 Percival Ln. Millbrook, NY 12545
brent.halloway@ridgefold-builders.com
www.ridgefold-builders.com
Residential contractor focused on design build, custom, and restoration projects. Emphasizing team concept
open to ideas possibly the logo

```html
<!DOCTYPE html>
<html lang="en">
<head>
<meta charset="utf-8">
<title>Ridgefold Builders — Stationery</title>
<link rel="stylesheet" href="https://fonts.googleapis.com/css2?family=Cinzel:wght@500&family=Lato:wght@400;700&display=swap">
<style>
  :root {
    --stage: #3b3b3d;
    --paper: #ffffff;
    --brown-dark: #3a1810;
    --brown: #5c2a19;
    --copper: #a55a32;
    --rule: #d9b9a4;
    --ghost: #f0ebe8;
    --ink: #4a2b20;
    --band-text: #e9d6c8;
  }
  * { margin: 0; padding: 0; box-sizing: border-box; }
  html, body { width: 1200px; height: 701px; overflow: hidden; background: var(--stage); }
  .canvas { position: relative; width: 1200px; height: 701px; background: var(--stage); }

  .sheet { position: absolute; background: var(--paper); box-shadow: 0 3px 10px rgba(0,0,0,.35); overflow: hidden; }

  .logo { position: absolute; display: flex; flex-direction: column; align-items: center; }
  .logo-square { width: 26px; height: 26px; background: var(--brown); }
  .logo-name {
    margin-top: 6px; font-family: "Cinzel", serif; font-weight: 500;
    font-size: 13px; color: var(--brown); letter-spacing: .5px; white-space: nowrap;
  }

  .ghost-mark { position: absolute; background: var(--ghost); }
  .footer-band {
    position: absolute; left: 0; right: 0; bottom: 0; background: var(--brown-dark);
    font-family: "Lato", sans-serif; font-size: 8px; color: var(--band-text);
    display: flex; align-items: center; padding-left: 12px; white-space: nowrap;
  }

  /* envelope back */
  .envelope-back { left: 77px; top: 146px; width: 390px; height: 290px; }
  .envelope-back svg { position: absolute; inset: 0; }
  .envelope-back .logo { left: 50%; top: 108px; transform: translateX(-50%); }
  .flap-name {
    position: absolute; left: 50%; top: 46px; transform: translateX(-50%);
    font-family: "Cinzel", serif; font-weight: 500; font-size: 11px; color: #f3e2d4; white-space: nowrap;
  }

  /* envelope front */
  .envelope-front { left: 137px; top: 341px; width: 451px; height: 199px; }
  .envelope-front .logo { left: 22px; top: 18px; }
  .envelope-front .ghost-mark { left: 232px; top: 40px; width: 100px; height: 100px; }
  .envelope-front .top-rule { position: absolute; left: 22px; width: 200px; top: 84px; height: 1px; background: var(--rule); }
  .envelope-front .footer-band { height: 20px; }

  /* letterhead */
  .letterhead { left: 473px; top: 12px; width: 410px; height: 583px; }
  .letterhead .logo { left: 50%; top: 20px; transform: translateX(-50%); }
  .letterhead .top-rule { position: absolute; left: 30px; right: 30px; top: 84px; height: 1px; background: var(--rule); }
  .letterhead .ghost-mark { left: 135px; top: 245px; width: 140px; height: 140px; }
  .letterhead .footer-band { height: 22px; justify-content: center; padding-left: 0; }

  /* business cards */
  .card-back {
    left: 1013px; top: 403px; width: 177px; height: 96px;
    background: radial-gradient(ellipse at 50% 45%, var(--copper) 0%, var(--brown) 55%, var(--brown-dark) 100%);
    display: flex; align-items: center; justify-content: center;
  }
  .card-back .logo-square { width: 18px; height: 18px; background: var(--paper); }

  .card-front { left: 900px; top: 504px; width: 208px; height: 96px; }
  .card-front .holder { position: absolute; left: 0; right: 0; top: 6px; text-align: center; font-family: "Lato", sans-serif; color: var(--copper); line-height: 1.2; }
  .card-front .holder-name { font-size: 7px; font-weight: 700; }
  .card-front .holder-title { font-size: 6px; }
  .card-front .logo { left: 50%; top: 25px; transform: translateX(-50%); }
  .card-front .logo-square { width: 14px; height: 14px; }
  .card-front .logo-name { margin-top: 3px; font-size: 8px; }
  .card-front .contact {
    position: absolute; left: 0; right: 0; top: 60px; text-align: center;
    font-family: "Lato", sans-serif; font-size: 5.5px; line-height: 1.35; color: var(--ink);
  }
  .card-front .footer-band { height: 7px; padding: 0; }
</style>
</head>
<body>
<main class="canvas">

  <section class="sheet envelope-back" aria-label="Envelope, back">
    <svg width="390" height="290" viewBox="0 0 390 290">
      <defs>
        <linearGradient id="flapFill" x1="0" y1="0" x2="0" y2="1">
          <stop offset="0" stop-color="#3a1810"/>
          <stop offset=".6" stop-color="#8a4526"/>
          <stop offset="1" stop-color="#b56a3e"/>
        </linearGradient>
      </defs>
      <polygon points="0,0 390,0 195,118" fill="url(#flapFill)"/>
      <polyline points="0,62 195,175 390,62" fill="none" stroke="#dcdcdc" stroke-width="1"/>
      <line x1="0" y1="290" x2="150" y2="190" stroke="#e4e4e4"/>
      <line x1="390" y1="290" x2="240" y2="190" stroke="#e4e4e4"/>
    </svg>
    <span class="flap-name">Ridgefold Builders</span>
    <div class="logo">
      <span class="logo-square"></span>
      <span class="logo-name">Ridgefold Builders</span>
    </div>
  </section>

  <section class="sheet envelope-front" aria-label="Envelope, front">
    <div class="logo">
      <span class="logo-square"></span>
      <span class="logo-name">Ridgefold Builders</span>
    </div>
    <div class="top-rule"></div>
    <div class="ghost-mark"></div>
    <div class="footer-band">38 Percival Ln. Ashford Falls, VT 05307</div>
  </section>

  <section class="sheet letterhead" aria-label="Letterhead">
    <div class="logo">
      <span class="logo-square"></span>
      <span class="logo-name">Ridgefold Builders</span>
    </div>
    <div class="top-rule"></div>
    <div class="ghost-mark"></div>
    <div class="footer-band">38 Percival Ln. Ashford Falls, VT 05307 &nbsp;|&nbsp; www.ridgefold-builders.com</div>
  </section>

  <section class="sheet card-back" aria-label="Business card, back">
    <span class="logo-square"></span>
  </section>

  <section class="sheet card-front" aria-label="Business card, front">
    <div class="holder">
      <div class="holder-name">Brent Halloway</div>
      <div class="holder-title">Project Manager</div>
    </div>
    <div class="logo">
      <span class="logo-square"></span>
      <span class="logo-name">Ridgefold Builders</span>
    </div>
    <div class="contact">
      38 Percival Ln. Ashford Falls, VT 05307<br>
      brent.halloway@ridgefold-builders.com<br>
      www.ridgefold-builders.com
    </div>
    <div class="footer-band"></div>
  </section>

</main>
</body>
</html>
```